Prepared Meal Delivery Website

Need a new modern design for a prepared meal delivery company that is hosted on Shopify.

Target Market(s)

Young Professionals

Industry/Entity Type

Prepared Meal Delivery Service

Number of Pages Required

5+ page

Requirements
Must have
• Use https://www.vorabelmeals.com/ as an example
Nice to have
• Vibrant page with call to action obvious and repeated
Should not have
• Generic look, grays/white/black

```html
<!DOCTYPE html>
<html lang="en">
<head>
<meta charset="utf-8">
<title>Stride Meals — Prepared Meal Delivery</title>
<link href="https://fonts.googleapis.com/css2?family=Poppins:wght@300;400;500;600;700;800&display=swap" rel="stylesheet">
<style>
:root{
  --orange:#f07a12;
  --orange-deep:#ea6a0a;
  --yellow:#ffc21a;
  --beige:#f7efe8;
  --ink:#1b1b1b;
  --body:#3c3c3c;
  --muted:#8a8a8a;
  --band:#f5f5f5;
}
*{box-sizing:border-box;margin:0;padding:0}
html,body{width:1200px;height:4521px;overflow:hidden}
body{position:relative;font-family:'Poppins',sans-serif;color:var(--ink);background:#fff}
.abs{position:absolute}
.txt{position:absolute;z-index:2}
.btn-solid{position:absolute;z-index:2;background:var(--orange);color:#fff;font-weight:600;font-size:15px;display:flex;align-items:center;justify-content:center;border-radius:4px}
.btn-outline{position:absolute;z-index:2;border:2px solid var(--orange);color:var(--orange);font-weight:600;font-size:15px;display:flex;align-items:center;justify-content:center;border-radius:30px;background:#fff}
.photo{position:absolute}
.brand{position:absolute;border:2px solid var(--ink);border-radius:4px;display:flex;align-items:center;justify-content:center;font-weight:600;letter-spacing:4px;color:var(--ink)}
.nav{position:absolute;top:42px;left:326px;display:flex;gap:44px;font-size:12.5px;font-weight:500}
.nav .active{border-bottom:2px solid var(--orange);padding-bottom:4px}
.section-title{position:absolute;z-index:2;left:0;width:1200px;text-align:center;font-size:33px;font-weight:400;letter-spacing:.5px}
.section-title b{font-weight:800}
.step-title{position:absolute;width:300px;text-align:center;color:var(--orange);font-weight:700;font-size:23px}
.step-text{position:absolute;width:300px;text-align:center;font-size:14px;line-height:23px;color:var(--body)}
.num{position:absolute;width:44px;height:44px;border-radius:50%;background:var(--orange);color:#fff;font-weight:700;font-size:15px;display:flex;align-items:center;justify-content:center}
.bag-item{position:absolute;width:220px;text-align:center;font-size:13px;font-weight:700;line-height:16px;color:#444}
.foot-h{position:absolute;font-size:15px;font-weight:700}
.foot-l{position:absolute;font-size:13px;line-height:26px;color:var(--body)}
.dot{position:absolute;width:30px;height:30px;border-radius:50%;background:var(--orange)}
</style>
</head>
<body>

<header>
  <div class="brand" style="left:86px;top:24px;width:190px;height:56px;font-size:17px">STRIDE MEALS</div>
  <nav class="nav">
    <span class="active">SHOP NOW</span><span>BUSINESS PLAN</span><span>GIFT CARDS</span><span>REWARDS</span><span>ABOUT US</span>
  </nav>
  <div class="btn-outline" style="left:920px;top:30px;width:126px;height:42px;border-radius:4px;font-size:12.5px;font-weight:500">CONTACT</div>
  <svg class="abs" style="left:1068px;top:40px" width="90" height="22" viewBox="0 0 90 22" fill="none" stroke="#222" stroke-width="2">
    <circle cx="8" cy="8" r="6"/><line x1="12.5" y1="12.5" x2="18" y2="18"/>
    <circle cx="44" cy="6" r="4"/><path d="M37 18c0-5 14-5 14 0z"/>
    <path d="M66 4h4l3 11h12l2-8H72"/><circle cx="75" cy="19" r="1.5"/><circle cx="84" cy="19" r="1.5"/>
  </svg>
</header>

<section class="hero">
  <div class="abs" style="left:0;top:96px;width:1200px;height:612px;background:var(--beige)"></div>
  <div class="photo" role="img" aria-label="Orange background with fresh vegetables" style="left:870px;top:96px;width:330px;height:612px;background:linear-gradient(160deg,#ff9a2a,#f0680a)"></div>
  <div class="photo" role="img" aria-label="Smiling man eating a prepared meal from a container" style="left:574px;top:150px;width:486px;height:470px;background:linear-gradient(150deg,#c9cbd2,#8aa5a3 55%,#6e7f86)"></div>
  <div class="abs" style="left:598px;top:175px;width:510px;height:445px;border:6px solid #fff"></div>
  <div class="abs" style="left:30px;top:510px;transform:rotate(-90deg);transform-origin:left top;font-size:24px;letter-spacing:3px;color:#cdc3bb;font-weight:300;white-space:nowrap">STRIDE MEALS</div>
  <div class="abs" style="left:103px;top:233px;width:40px;height:300px;border:3px solid var(--orange);border-right:none"></div>
  <h1 class="txt" style="left:136px;top:272px;font-size:46px;line-height:52px;font-weight:800">EMPLOWERING<br><span style="color:var(--orange)">ATHELETES</span></h1>
  <p class="txt" style="left:136px;top:393px;width:400px;font-size:15px;line-height:19px;color:var(--body)">Get into the best shape of your life with delicious, science-backed meals designed for results.</p>
  <div class="btn-solid" style="left:140px;top:449px;width:172px;height:48px">SHOP NOW</div>
  <div class="photo" role="img" aria-label="Two black meal trays with grilled chicken and salad" style="left:318px;top:520px;width:400px;height:185px;border-radius:40px;background:radial-gradient(ellipse at 40% 40%,#7fb04a,#2a2a2a 70%)"></div>
</section>

<section class="about">
  <div class="abs" style="left:0;top:820px;width:430px;height:498px;background:var(--yellow)"></div>
  <div class="photo" role="img" aria-label="Woman holding a healthy meal" style="left:76px;top:771px;width:273px;height:254px;background:linear-gradient(150deg,#8a8d94,#d9d3cf)"></div>
  <div class="photo" role="img" aria-label="Man eating a meal at a table" style="left:369px;top:878px;width:218px;height:204px;background:linear-gradient(150deg,#e9e6e2,#5a6b84)"></div>
  <div class="photo" role="img" aria-label="Meal container with rice, beans and vegetables" style="left:132px;top:1045px;width:218px;height:205px;background:linear-gradient(150deg,#d9b07d,#b84a22)"></div>
  <div class="photo" role="img" aria-label="Tray of meatballs and roasted vegetables" style="left:373px;top:1104px;width:174px;height:164px;background:linear-gradient(150deg,#d9c7a7,#8b3a1c)"></div>
  <h2 class="txt" style="left:600px;top:880px;width:520px;text-align:center;font-size:36px;line-height:46px;font-weight:400">ABOUT <b style="font-weight:800">STRIDE</b><br><b style="font-weight:800">MEALS</b></h2>
  <p class="txt" style="left:640px;top:1002px;width:440px;text-align:center;font-size:15.5px;line-height:27px;color:var(--body)">Lorem ipsum dolor sit amet, consectetur adipiscing elit, sed do eiusmod tempor incididunt ut labore et dolore magna aliqua. Ut enim ad minim veniam.Lorem ipsum dolor sit amet, consectetur adipiscing elit, sed do eiusmod tem</p>
  <div class="btn-outline" style="left:767px;top:1167px;width:198px;height:54px">CHOOSE A PLAN</div>
</section>

<section class="press">
  <div class="abs" style="left:0;top:1318px;width:1200px;height:122px;background:var(--band)"></div>
  <svg class="abs" style="left:95px;top:1360px" width="1020" height="40" viewBox="0 0 1020 40" fill="#c9c9c9">
    <rect x="4" y="8" width="80" height="24" rx="3"/>
    <rect x="126" y="6" width="112" height="28" rx="3"/>
    <rect x="283" y="6" width="34" height="28" rx="3"/>
    <rect x="365" y="6" width="20" height="28" rx="3"/>
    <circle cx="451" cy="20" r="14"/>
    <rect x="515" y="8" width="64" height="24" rx="3"/>
    <rect x="617" y="6" width="140" height="28" rx="3"/>
    <rect x="800" y="6" width="220" height="28" rx="3"/>
  </svg>
</section>

<section class="how">
  <h2 class="section-title" style="top:1498px">HOW STRIDE <b>MEAL WORKS</b></h2>
  <div class="abs" style="left:551px;top:1554px;width:50px;height:3px;background:var(--orange)"></div>
  <svg class="abs" style="left:0;top:1590px" width="1200" height="290" viewBox="0 0 1200 290" fill="none" stroke="var(--orange)" stroke-width="2">
    <path d="M136 150 A124 124 0 0 1 384 150"/>
    <path d="M720 150 A124 124 0 0 1 480 150" transform="rotate(180 600 150)"/>
    <path d="M830 150 A124 124 0 0 1 1078 150"/>
    <line x1="384" y1="150" x2="476" y2="150"/>
    <line x1="724" y1="150" x2="830" y2="150"/>
  </svg>
  <div class="photo" role="img" aria-label="Laptop showing meal choices on an orange background" style="left:145px;top:1624px;width:230px;height:230px;border-radius:50%;background:linear-gradient(160deg,#f27d14,#f6a24a 55%,#9b6a3d 56%,#7d5a3a)"></div>
  <div class="photo" role="img" aria-label="Woman collecting a delivery bag in her kitchen" style="left:485px;top:1624px;width:230px;height:230px;border-radius:50%;background:linear-gradient(160deg,#e5e5e5,#6a6a6a 60%,#2a2a2a)"></div>
  <div class="photo" role="img" aria-label="Bowl of salad with cucumber and carrots" style="left:840px;top:1624px;width:230px;height:230px;border-radius:50%;background:radial-gradient(circle at 50% 50%,#8fbf4a,#e98a3a 55%,#4c5e3a)"></div>
  <div class="num" style="left:245px;top:1594px">01</div>
  <div class="num" style="left:578px;top:1826px">02</div>
  <div class="num" style="left:935px;top:1580px">03</div>
  <div class="step-title" style="left:110px;top:1886px">Choose a Plan</div>
  <div class="step-text" style="left:110px;top:1928px">Choose one of our pre-set plans, or Build Your Own!</div>
  <div class="step-title" style="left:455px;top:1886px">Await Delivery</div>
  <div class="step-text" style="left:455px;top:1928px">We deliver twice weekly, on Sundays and Wednesdays Our delivery window is between 3 pm and 8 pm</div>
  <div class="step-title" style="left:808px;top:1886px">Heat &amp; Eat</div>
  <div class="step-text" style="left:808px;top:1928px">Place your meal in the microwave for 2-2.5 minutes or reheat to preferred temperature on a pan/skillet</div>
  <div class="btn-outline" style="left:506px;top:2042px;width:198px;height:54px">CHOOSE A PLAN</div>
</section>

<section class="who">
  <div class="photo" role="img" aria-label="Orange background with faint food textures" style="left:0;top:2165px;width:1200px;height:475px;background:linear-gradient(100deg,var(--orange-deep),#f78d1d 55%,var(--yellow))"></div>
  <h2 class="section-title" style="top:2225px;color:#fff">WHO IS <b>STRIDE FOR ?</b></h2>
  <div class="abs" style="left:563px;top:2280px;width:74px;height:3px;background:#fff"></div>
  <p class="txt" style="left:300px;top:2296px;width:600px;text-align:center;color:#fff;font-size:17px;line-height:26px">Lorem ipsum dolor sit amet, consectetur adipiscing elit, sed do eiusmod tempor incididunt ut labore et dolore</p>
  <div class="abs" style="left:521px;top:2370px;width:160px;height:44px;border:2px solid #fff;border-radius:24px;color:#fff;font-size:13px;font-weight:600;display:flex;align-items:center;justify-content:center">START PLAN</div>
  <div class="photo" role="img" aria-label="Muscular man in a tank top at the gym" style="left:130px;top:2475px;width:308px;height:260px;background:linear-gradient(150deg,#9b9b9b,#3a3a3a)"></div>
  <div class="photo" role="img" aria-label="Woman in sportswear at the gym" style="left:770px;top:2475px;width:308px;height:260px;background:linear-gradient(150deg,#f0f0f0,#6a6a6a)"></div>
  <div class="photo" role="img" aria-label="Mother and daughter smiling together" style="left:440px;top:2452px;width:326px;height:305px;background:linear-gradient(150deg,#8a7a6e,#3d3633);border:3px solid #fff"></div>
  <div class="abs" style="left:440px;top:2452px;width:326px;height:305px;background:rgba(30,30,30,.55)"></div>
  <div class="abs" style="left:563px;top:2493px;width:80px;height:80px;border-radius:50%;background:var(--orange);border:3px solid #fff"></div>
  <svg class="abs" style="left:583px;top:2511px" width="40" height="40" viewBox="0 0 40 40" fill="none" stroke="#fff" stroke-width="2"><circle cx="13" cy="12" r="6"/><circle cx="27" cy="12" r="6"/><path d="M3 36c0-9 20-9 20 0M17 36c0-9 20-9 20 0"/></svg>
  <div class="abs" style="left:440px;top:2580px;width:326px;text-align:center;color:#fff;font-weight:700;font-size:17px">FAMILIES</div>
  <p class="abs" style="left:470px;top:2616px;width:266px;text-align:center;color:#fff;font-size:12.5px;line-height:19px">Set your family up for success with a week of healthy meals planned ahead. By ordering the week before, you'll be able to able to serve your family healthy meals with minimal effort!</p>
  <svg class="abs" style="left:256px;top:2655px" width="50" height="40" viewBox="0 0 50 40" fill="none" stroke="#fff" stroke-width="2"><circle cx="25" cy="10" r="7"/><path d="M8 38c0-12 34-12 34 0"/></svg>
  <div class="abs" style="left:130px;top:2698px;width:308px;text-align:center;color:#fff;font-weight:700;font-size:18px">PROFESSIONAL</div>
  <svg class="abs" style="left:899px;top:2648px" width="50" height="40" viewBox="0 0 50 40" fill="none" stroke="#fff" stroke-width="2"><circle cx="25" cy="10" r="7"/><path d="M8 38c0-12 34-12 34 0"/></svg>
  <div class="abs" style="left:770px;top:2694px;width:308px;text-align:center;color:#fff;font-weight:700;font-size:18px">SINGLES</div>
</section>

<section class="bag">
  <h2 class="section-title" style="top:2845px">WHAT'S IN <b>YOUR STRIDE BAG ?</b></h2>
  <div class="abs" style="left:551px;top:2900px;width:86px;height:3px;background:var(--orange)"></div>
  <svg class="abs" style="left:0;top:2945px" width="1200" height="70" viewBox="0 0 1200 70" fill="none" stroke="var(--orange)" stroke-width="2.5">
    <path d="M205 40h60M210 40a25 20 0 0 0 50 0M222 30c-4-6 4-8 0-14M235 30c-4-6 4-8 0-14M248 30c-4-6 4-8 0-14"/>
    <rect x="432" y="12" width="46" height="48"/><rect x="440" y="20" width="30" height="14"/><line x1="440" y1="44" x2="470" y2="44"/><line x1="440" y1="52" x2="470" y2="52"/>
    <path d="M695 60V30M695 40c-12 0-16-12-16-18 8 0 16 6 16 18zM695 36c12 0 16-10 16-16-8 0-16 6-16 16zM683 60h24"/>
    <path d="M975 12l14 24h-28zM961 48l-10-18M989 48l10-18M955 56h40"/>
  </svg>
  <div class="bag-item" style="left:128px;top:3030px">DELICIOUS<br>CHEF-INSPIRED MEALS</div>
  <div class="abs" style="left:140px;top:3080px;width:196px;height:3px;background:var(--orange)"></div>
  <div class="bag-item" style="left:352px;top:3030px;color:#666">PERFECTLY PORTIONED<br>AMOUNTS</div>
  <div class="bag-item" style="left:593px;top:3030px;color:#666">RESPONSIBLY SOURCED,<br>QUALITY INGREDIENTS</div>
  <div class="bag-item" style="left:863px;top:3030px;color:#666">RECYCLABLE ICE PACKS<br>AND PACKAGING</div>

  <h3 class="txt" style="left:136px;top:3188px;font-size:29px;line-height:38px;font-weight:800;color:var(--orange)">DELICIOUS<br>CHEF-INSPIRED MEALS</h3>
  <p class="txt" style="left:136px;top:3285px;width:440px;font-size:16.5px;line-height:30px;color:var(--body)">Our meals are designed and prepared by a team of experienced chefs with decades of experience and a passion for preparing food that is healthy, macro-nutrient friendly, yet doesn't compromise on flavor.</p>
  <div class="btn-outline" style="left:136px;top:3425px;width:198px;height:56px">CHOOSE A PLAN</div>
  <div class="abs" style="left:608px;top:3122px;width:456px;height:456px;border-radius:50%;border:2px solid var(--orange)"></div>
  <div class="photo" role="img" aria-label="Plate of beef, rice noodles, peppers, broccoli and lime" style="left:630px;top:3144px;width:412px;height:412px;border-radius:50%;background:radial-gradient(circle at 45% 45%,#f0ece4 0,#c8824a 40%,#4f7d2e 75%,#e8e8e8 76%)"></div>
  <div class="abs" style="left:626px;top:3425px;width:112px;height:112px;border-radius:50%;background:var(--orange)"></div>
  <svg class="abs" style="left:652px;top:3455px" width="60" height="50" viewBox="0 0 60 50" fill="none" stroke="#fff" stroke-width="2.5"><path d="M5 32h50M10 32a20 14 0 0 0 40 0M22 22c-4-6 4-8 0-14M30 22c-4-6 4-8 0-14M38 22c-4-6 4-8 0-14"/></svg>
</section>

<section class="cta">
  <div class="photo" role="img" aria-label="Faded background of meal containers" style="left:0;top:3635px;width:1200px;height:535px;background:linear-gradient(90deg,#f3e6d8,#f6efe6)"></div>
  <div class="abs" style="left:0;top:3635px;width:373px;height:535px;background:linear-gradient(180deg,var(--yellow),#ffb000)"></div>
  <div class="abs" style="left:98px;top:3688px;width:510px;height:485px;border:5px solid #fff"></div>
  <div class="photo" role="img" aria-label="Woman in workout clothes doing a push-up" style="left:110px;top:3800px;width:520px;height:300px;border-radius:60px;background:linear-gradient(160deg,#e2a46a,#3a3a3a 55%,#2d6ea8)"></div>
  <h2 class="txt" style="left:670px;top:3780px;font-size:33px;line-height:42px;font-weight:400">WHAT ARE YOU<br><b style="font-weight:800">WAITING FOR?</b></h2>
  <div class="abs" style="left:670px;top:3870px;width:74px;height:3px;background:var(--orange)"></div>
  <p class="txt" style="left:670px;top:3882px;width:420px;font-size:15.5px;line-height:28px;color:var(--body)">Lorem ipsum dolor sit amet, consectetur adipiscing elit, sed do eiusmod tempor incididunt ut</p>
  <div class="btn-solid" style="left:670px;top:3955px;width:184px;height:48px;border-radius:26px">GET STARTED</div>
  <div class="photo" role="img" aria-label="Black meal tray with chicken and fresh vegetables" style="left:805px;top:4015px;width:295px;height:140px;border-radius:30px;background:radial-gradient(ellipse at 50% 35%,#8fbf4a,#222 65%)"></div>
</section>

<footer>
  <div class="brand" style="left:115px;top:4240px;width:210px;height:58px;font-size:18px">STRIDE MEALS</div>
  <p class="abs" style="left:116px;top:4330px;font-size:12.5px;line-height:23px;color:var(--body)">© 2022 Stride Meals<br>All Rights Reserved</p>
  <div class="abs" style="left:405px;top:4175px;width:1px;height:230px;background:#e5e5e5"></div>
  <div class="abs" style="left:607px;top:4175px;width:1px;height:230px;background:#e5e5e5"></div>
  <div class="abs" style="left:843px;top:4175px;width:1px;height:230px;background:#e5e5e5"></div>
  <div class="foot-h" style="left:427px;top:4245px">QUICK LINKS</div>
  <div class="foot-l" style="left:427px;top:4280px">About<br>Shop Now<br>Business Plan<br>Gift Cards<br>Contact</div>
  <div class="foot-h" style="left:630px;top:4245px">CONTACT US</div>
  <div class="dot" style="left:631px;top:4288px"></div>
  <svg class="abs" style="left:638px;top:4295px" width="16" height="16" viewBox="0 0 16 16" fill="#fff"><path d="M3 1l3 3-2 2c1 2 3 4 5 5l2-2 3 3-2 3C6 14 1 8 1 3z"/></svg>
  <div class="foot-l" style="left:671px;top:4290px">hello@stridemeals.com</div>
  <div class="dot" style="left:631px;top:4328px"></div>
  <svg class="abs" style="left:637px;top:4337px" width="18" height="13" viewBox="0 0 18 13" fill="none" stroke="#fff" stroke-width="1.6"><rect x="1" y="1" width="16" height="11"/><path d="M1 1l8 6 8-6"/></svg>
  <div class="foot-l" style="left:671px;top:4328px">(555) 010 4821</div>
  <div class="foot-h" style="left:872px;top:4245px">JOIN COMMUNITY</div>
  <div class="foot-l" style="left:872px;top:4280px">Sign up now and get best offers.</div>
  <div class="abs" style="left:868px;top:4319px;width:240px;height:42px;border:1.5px solid var(--orange);border-radius:22px;font-size:12px;color:var(--body);padding:11px 0 0 22px">Email address</div>
  <div class="abs" style="left:1056px;top:4319px;width:53px;height:42px;background:var(--orange);border-radius:0 22px 22px 0"></div>
  <svg class="abs" style="left:1070px;top:4331px" width="26" height="18" viewBox="0 0 26 18" fill="none" stroke="#fff" stroke-width="2"><path d="M2 9h20M15 2l7 7-7 7"/></svg>
  <div class="dot" style="left:870px;top:4376px;background:var(--orange)"></div>
  <div class="dot" style="left:904px;top:4376px;background:#b9c8d8"></div>
  <div class="dot" style="left:938px;top:4376px;background:#b9c8d8"></div>
  <div class="dot" style="left:972px;top:4376px;background:#b9c8d8"></div>
</footer>

</body>
</html>
```